Flyer marketing document - Kessway LMR Engineering

We need a more modern version of a marketing flyer/ brochures for our business and service offering. I would like an overall business brochure, plus potentially some examples of specific parts of the business. The brochure attached provides a fairly detailed overview of the business. We need to extract what the core offering is and have the ability to sell to the market this offering, around the innovative design, engineering and manufacture of the equipment we offer.

```html
<!DOCTYPE html>
<html lang="en">
<head>
<meta charset="utf-8">
<title>Service Truck Brochure Spread</title>
<link href="https://fonts.googleapis.com/css2?family=Open+Sans:wght@400;600&display=swap" rel="stylesheet">
<style>
  :root {
    --backdrop: #5e5e5e;
    --paper: #ffffff;
    --paper-shade: #ececec;
    --ink: #3d3d3d;
    --band-dark: #2a2a2a;
    --band-red: #c8323c;
    --sky: #8fb3d8;
    --sky-light: #d9e4ee;
    --machine: #b69a4e;
    --ground: #7a7065;
    --tank-red: #c23a32;
    --tank-orange: #d9673a;
    --panel-grey: #9a9fa5;
  }
  * { box-sizing: border-box; margin: 0; padding: 0; }
  html, body { width: 1200px; height: 900px; overflow: hidden; }
  body {
    background: var(--backdrop);
    font-family: "Open Sans", sans-serif;
    color: var(--ink);
  }
  .spread {
    position: absolute;
    left: 40px; top: 54px;
    width: 1120px; height: 792px;
    display: flex;
    box-shadow: 0 10px 30px rgba(0,0,0,.35);
  }
  .page {
    position: relative;
    width: 560px; height: 792px;
    overflow: hidden;
  }
  .page--left { background: linear-gradient(90deg, var(--paper) 85%, var(--paper-shade)); }
  .page--right { background: linear-gradient(90deg, var(--paper-shade), var(--paper) 15%, var(--paper) 80%, var(--paper-shade)); }
  .hero { position: absolute; left: 0; top: 0; width: 560px; height: 320px; }
  .photo { position: absolute; }
  .photo--red-tank { background: linear-gradient(180deg, var(--sky) 0%, var(--sky-light) 35%, var(--tank-red) 55%, #6a5f58 100%); }
  .photo--orange-truck { background: linear-gradient(180deg, #8c8a88 0%, #6f6b68 45%, var(--tank-orange) 70%, #5b5652 100%); }
  .photo--compressor { background: linear-gradient(135deg, #e7b63a 0%, #f4f1ec 45%, #d34a3f 80%, #6b6b6b 100%); }
  .photo--controls { background: radial-gradient(circle at 45% 50%, var(--panel-grey) 0%, #6d7177 55%, #1e2a4a 100%); }
  .photo--yard-truck { background: linear-gradient(180deg, var(--sky) 0%, var(--sky-light) 40%, var(--machine) 62%, var(--ground) 100%); }
  .photo--cabinet { background: linear-gradient(135deg, #d9a94b 0%, #3c3a37 50%, #c8a45a 100%); }
  .photo--access { background: linear-gradient(180deg, var(--sky) 0%, var(--sky-light) 40%, var(--machine) 65%, #5a544c 100%); }
  .copy {
    position: absolute;
    text-align: justify;
    line-height: 1.3;
  }
  .copy--lg { font-size: 12px; }
  .copy--md { font-size: 11px; }
  .copy--sm { font-size: 10px; text-align: left; }
</style>
</head>
<body>
  <main class="spread">
    <section class="page page--left">
      <svg class="hero" viewBox="0 0 560 320">
        <defs>
          <linearGradient id="heroSkyLeft" x1="0" y1="0" x2="0" y2="1">
            <stop offset="0" stop-color="#7fa6d0"/>
            <stop offset=".45" stop-color="#dce6ef"/>
            <stop offset=".7" stop-color="#b69a4e"/>
            <stop offset="1" stop-color="#6e665c"/>
          </linearGradient>
        </defs>
        <path d="M0 0H560V170Q300 230 0 300Z" fill="url(#heroSkyLeft)" role="img" aria-label="Photo: two mining service trucks with tank bodies on a mine site under a cloudy sky"/>
        <path d="M0 300Q300 230 560 170V182Q300 244 0 318Z" fill="var(--band-dark)"/>
      </svg>

      <div class="photo photo--red-tank" style="left:30px;top:335px;width:250px;height:135px" role="img" aria-label="Photo: red service tank body loaded on a transport trailer"></div>
      <p class="copy copy--lg" style="left:30px;top:478px;width:250px">Service trucks use reliable and successful layouts for the product tanks and dispensing equipment. High flow diesel pumps have NMI compliant metering and recording equipment. Simple to use and designed for maximum Reliability.</p>

      <div class="photo photo--orange-truck" style="left:30px;top:575px;width:250px;height:135px" role="img" aria-label="Photo: orange articulated service truck parked on a mine haul road"></div>
      <p class="copy copy--lg" style="left:30px;top:718px;width:250px">Unlike some of our competitors our TANK layouts allow for the use of standard wheel base trucks and maximise each trucks carrying capacity.</p>

      <div class="photo photo--compressor" style="left:300px;top:270px;width:235px;height:130px" role="img" aria-label="Photo: hydraulic drive screw air compressor mounted behind a yellow handrail"></div>
      <p class="copy copy--md" style="left:300px;top:408px;width:235px">We use Hydraulic drive screw air compressor with air capacity available upto 165 cfm. Low maintenance with no diesel drive engine to service or "rattle apart". Hydraulic control systems allow the outputs of the fuel and pneumatic systems to be varied as required.</p>

      <div class="photo photo--controls" style="left:300px;top:520px;width:235px;height:140px" role="img" aria-label="Photo: control panel with gauges, switches and a red stop button"></div>
      <p class="copy copy--md" style="left:300px;top:668px;width:235px">Control systems are simple to use, with comonentry readily available ensuring that spare parts can be easily obtained to keep your equipment operable.</p>
    </section>

    <section class="page page--right">
      <svg class="hero" viewBox="0 0 560 320">
        <defs>
          <linearGradient id="heroSkyRight" x1="0" y1="0" x2="0" y2="1">
            <stop offset="0" stop-color="#7fa6d0"/>
            <stop offset=".4" stop-color="#dde7f0"/>
            <stop offset=".65" stop-color="#b69a4e"/>
            <stop offset="1" stop-color="#7a7065"/>
          </linearGradient>
        </defs>
        <path d="M0 0H560V120Q260 130 0 210Z" fill="url(#heroSkyRight)" role="img" aria-label="Photo: two yellow service trucks parked side by side in a yard"/>
        <path d="M0 210Q260 130 560 120V132Q260 146 0 226Z" fill="var(--band-red)"/>
      </svg>

      <div class="photo photo--yard-truck" style="left:40px;top:240px;width:235px;height:125px" role="img" aria-label="Photo: yellow service truck with side cabinets"></div>
      <p class="copy copy--sm" style="left:300px;top:178px;width:230px">Proven Tank design and cabinet layouts, transportation issues and dimensional considerations made at the design stage reduce costs of moving plant around the country</p>

      <div class="photo photo--cabinet" style="left:40px;top:375px;width:235px;height:130px" role="img" aria-label="Photo: open service cabinet with hose reels and fittings"></div>
      <p class="copy copy--sm" style="left:300px;top:310px;width:230px">Our in house design team ensure All possible options and client requirements considered and incorporated in thier project. 30 Years of design experience ensures only the best solutions are put forward and incorporated.</p>

      <div class="photo photo--access" style="left:40px;top:515px;width:235px;height:140px" role="img" aria-label="Photo: service truck under a workshop dome showing access steps and platforms"></div>
      <p class="copy copy--sm" style="left:300px;top:480px;width:230px">Large access areas with properly designed and manufactured steps and platforms give the best maintenance opportunity</p>
    </section>
  </main>
</body>
</html>
```